Wordpress theme customised please - for new ecommerce homewares website

Hi, we need a wordpress theme customised for a business that will sell tea towels (aka kitchen towels/dish cloths).
We do not have a website currently, but wish to launch using wordpress + woocommerce + "the marrowfen" theme (c/- getplumwick).
BACKGROUND RE THE BUSINESS
Our products are very stylish and will appeal to people who like owning gorgeous things - people who love cooking and/or decorating their home beautifully, or maybe they like travelling and/or buying presents for themselves and friends/family etc.
As they are typically used in people's kitchens, so "fresh" and "clean" is important - however the site must look very upmarket: timeless yet current, and classic yet simple, but not pretty, fussy or edgy.
We believe we have a great opportunity to leverage the "feel" of the product - cotton & linen fabric that has real texture to it, is tactile, natural, raw, real... in the photos used on the website, the backgrounds etc
Our logo is attached - a very dark grey colour was chosen, with white stripes, so that its neutral colouring would coordinate well with our suppliers' existing packaging. (We will represent a number of brands.)
BACKGROUND RE THIS PROJECT
We already know we want to use "the marrowfen" theme by getplumwick, but we need help customising the look of this theme so it works well with our logo, looks really striking and doesn't look like everyone else's ie "straight out of the box".
It appears these are the types of things that can be changed:
LAYOUT:
home page design concept (eg with a kestrel carousel)
page design concept for eg About Us, Contact Us, FAQs
landing page design concept
header; light footer; dark footer
COLOURS & BACKGROUNDS & BORDERS & SEPARATORS:
main theme colour; accent colour; primary font colour
header background; light footer background colour; dark footer background colour; copyright bar background colour
dark footer widget title border; dark footer list separators and borders; dark footer/copyright bar separator styles
FONTS:
main navigation text colour; secondary navigation text colour; dark footer text colour; copyright bar text colour
main font; secondary font
LASTLY
Please don't hesitate to ask questions, request further information etc This is the first time we've posted a design project like this so it's tricky to know what other information you will need, so please just get in touch, ok!
Thanks so much for your interest in this project, and best wishes.

```html
<!DOCTYPE html>
<html lang="en">
<head>
<meta charset="utf-8">
<title>Clothline House — Home</title>
<link rel="stylesheet" href="https://fonts.googleapis.com/css2?family=Arvo:wght@400;700&family=Lato:wght@400;700;900&family=Playfair+Display:wght@500&display=swap">
<style>
:root{
  --ink:#262d3b;
  --topbar:#f3f3f3;
  --text:#1c1c1c;
  --muted:#8a8a8a;
  --accent:#6b7a9b;
  --badge:#8593b4;
  --rule:#d9d9d9;
  --white:#ffffff;
}
*{box-sizing:border-box;margin:0;padding:0}
html,body{width:1200px;height:900px;overflow:hidden;background:var(--white);color:var(--text);font-family:"Lato",sans-serif}
.canvas{position:relative;width:1200px;height:900px}
.topbar{position:absolute;left:0;top:0;width:1200px;height:75px;background:var(--topbar)}
.main-nav{position:absolute;left:508px;top:21px;display:flex;gap:18px;padding-bottom:6px;border-bottom:1px solid #bdbdbd;width:342px}
.main-nav span{font:900 10px "Lato",sans-serif;color:var(--text);letter-spacing:.2px;white-space:nowrap}
.main-nav span::after{content:"";display:inline-block;width:4px;height:4px;border-right:1.5px solid #333;border-bottom:1.5px solid #333;transform:rotate(45deg);margin-left:8px;position:relative;top:-3px}
.sub-nav{position:absolute;left:609px;top:44px;font:400 10.5px "Arvo",serif;color:var(--muted);white-space:nowrap}
.sub-nav i{font-style:normal;margin:0 8px}
.bag{position:absolute;left:875px;top:15px;width:106px;height:50px;border:1px solid #cfcfcf;background:var(--white);padding:7px 7px}
.bag-title{font:900 10px "Lato",sans-serif;padding-bottom:6px;border-bottom:1px solid #ddd;position:relative}
.bag-title::after{content:"";position:absolute;right:4px;top:1px;width:4px;height:4px;border-right:1.5px solid #333;border-bottom:1.5px solid #333;transform:rotate(45deg)}
.bag-meta{font:400 10px "Arvo",serif;color:var(--muted);margin-top:6px;white-space:nowrap}
.bag-meta i{font-style:normal;margin:0 6px}
.masthead{position:absolute;left:0;top:75px;width:1200px;height:51px}
.stripe{position:absolute;left:0;width:1200px;background:var(--ink)}
.brand{position:absolute;left:214px;top:80px;font:500 33px "Playfair Display",serif;color:var(--white);letter-spacing:.5px;white-space:nowrap;line-height:40px}
.util-links{position:absolute;left:642px;top:95px;font:700 8.5px "Lato",sans-serif;color:var(--white);white-space:nowrap}
.util-links span+span{margin-left:16px}
.search{position:absolute;left:809px;top:88px;width:144px;height:23px;background:var(--white)}
.search-btn{position:absolute;left:955px;top:88px;width:26px;height:23px;border-right:1px solid #5a6170}
.banner{position:absolute;top:148px;width:245px;height:368px;overflow:hidden}
.banner-photo{position:absolute;inset:0}
.banner-frame{position:absolute;left:9px;top:9px;right:9px;bottom:9px;background:rgba(140,140,140,.35)}
.banner-copy{position:absolute;left:0;right:0;top:155px;text-align:center;color:var(--white)}
.banner-title{font:700 17px "Arvo",serif;letter-spacing:.3px}
.banner-copy hr{width:58px;border:0;border-top:1.5px solid var(--white);margin:9px auto 11px}
.banner-sub{font:400 10.5px "Arvo",serif}
.divider{position:absolute;left:214px;top:538px;width:767px;border-top:1px solid var(--rule)}
.section-title{position:absolute;left:215px;top:560px;font:700 10.5px "Arvo",serif;letter-spacing:.2px}
.section-mark{position:absolute;left:214px;top:594px;width:49px;border-top:2px solid var(--text)}
.carousel-nav{position:absolute;left:917px;top:553px}
.product{position:absolute;top:621px;width:160px}
.product-photo{width:155px;height:198px}
.badge{position:absolute;left:107px;top:-8px;width:37px;height:37px;border-radius:50%;background:var(--badge);color:var(--white);font:italic 700 8px "Lato",sans-serif;display:flex;align-items:center;justify-content:center}
.product-brand{margin-top:9px;font:700 9.5px "Lato",sans-serif;color:var(--accent);text-transform:uppercase;letter-spacing:.2px}
.product-name{margin-top:3px;font:400 10px "Arvo",serif}
.price{margin-top:4px;font:900 14px "Lato",sans-serif;white-space:nowrap}
.price sup{font-size:8px;vertical-align:5px}
.price s{font:400 10.5px "Lato",sans-serif;color:#777;margin-right:6px}
</style>
</head>
<body>
<div class="canvas">
  <header class="topbar">
    <nav class="main-nav"><span>HOME</span><span>SHOP BY</span><span>ALL PAGES</span><span>SHORTCODES</span><span>BLOG</span></nav>
    <div class="sub-nav">All Products<i>|</i>Lookbook<i>|</i>Sales<i>|</i>Gift Cards</div>
    <div class="bag">
      <div class="bag-title">SHOPPING BAG</div>
      <div class="bag-meta">€66.94<i>/</i>2 Items</div>
    </div>
  </header>

  <div class="masthead">
    <div class="stripe" style="top:0;height:3px"></div>
    <div class="stripe" style="top:6px;height:37px"></div>
    <div class="stripe" style="top:46px;height:4px"></div>
  </div>
  <div class="brand">CLOTHLINE HOUSE</div>
  <div class="util-links"><span>TRACK YOUR ORDER</span><span>MY ACCOUNT</span></div>
  <div class="search"></div>
  <div class="search-btn">
    <svg width="26" height="23" viewBox="0 0 26 23"><circle cx="12" cy="10.5" r="3.6" fill="none" stroke="#fff" stroke-width="1.6"/><line x1="14.6" y1="13.1" x2="17" y2="15.5" stroke="#fff" stroke-width="1.8"/></svg>
  </div>

  <a class="banner" style="left:214px">
    <div class="banner-photo" role="img" aria-label="Linen tea towels with black geometric and dotted prints hanging on pegs" style="background:linear-gradient(160deg,#e4e0d9,#cfc8bd 55%,#b7ae9f)"></div>
    <div class="banner-copy"><div class="banner-title">SHOP SALE</div><hr><div class="banner-sub">The sale don't stop up to 75% off!</div></div>
  </a>
  <a class="banner" style="left:475px">
    <div class="banner-photo" role="img" aria-label="Grey and orange striped tea towels hanging on pegs" style="background:linear-gradient(120deg,#b9b6b1,#c9bcad 50%,#d49a6c)"></div>
    <div class="banner-frame"></div>
    <div class="banner-copy"><div class="banner-title">ACCESSORIES</div><hr><div class="banner-sub">The sale don't stop up to 75% off!</div></div>
  </a>
  <a class="banner" style="left:736px">
    <div class="banner-photo" role="img" aria-label="White tea towels with coloured lettered stripes in grey, green, orange and pink" style="background:linear-gradient(100deg,#d9d6d0,#dfe3d4 35%,#eebc93 65%,#d99bc0)"></div>
    <div class="banner-copy"><div class="banner-title">LOOKBOOK</div><hr><div class="banner-sub">Take a look at the upcoming trends.</div></div>
  </a>

  <div class="divider"></div>
  <div class="section-title">FEATURED PRODUCTS</div>
  <div class="section-mark"></div>
  <svg class="carousel-nav" width="66" height="30" viewBox="0 0 66 30">
    <circle cx="15" cy="15" r="13.5" fill="none" stroke="#9a9a9a" stroke-width="1.2"/>
    <polyline points="17.5,10 12.5,15 17.5,20" fill="none" stroke="#777" stroke-width="1.2"/>
    <circle cx="49" cy="15" r="13.5" fill="none" stroke="#9a9a9a" stroke-width="1.2"/>
    <polyline points="46.5,10 51.5,15 46.5,20" fill="none" stroke="#777" stroke-width="1.2"/>
  </svg>

  <article class="product" style="left:213px">
    <div class="product-photo" role="img" aria-label="Stack of folded white tea towels with green stripes" style="background:linear-gradient(180deg,#f4f3ef 30%,#8e9b84 75%,#4f6146)"></div>
    <div class="product-brand">Everyday Stripe</div>
    <div class="product-name">Beanie Hat</div>
    <div class="price">€ 24<sup>.00</sup></div>
  </article>
  <article class="product" style="left:410px">
    <div class="product-photo" role="img" aria-label="Stack of folded natural linen tea towels with plum stripes" style="background:linear-gradient(180deg,#d9d3cb,#bfae9e 45%,#8e5c74 80%,#c9c2bc)"></div>
    <div class="badge">SALE</div>
    <div class="product-brand">Easy as Pie</div>
    <div class="product-name">Check Shirt</div>
    <div class="price"><s>€112.92</s>€ 67<sup>.75</sup></div>
  </article>
  <article class="product" style="left:611px">
    <div class="product-photo" role="img" aria-label="White waffle tea towels draped over a wooden crate with a ball of twine" style="background:linear-gradient(150deg,#eeeae3,#d5ccc0 50%,#7a5a42)"></div>
    <div class="product-brand">Keep It Simple</div>
    <div class="product-name">High Top Trainers</div>
    <div class="price"><s>€77.63</s>€ 46<sup>.58</sup></div>
  </article>
  <article class="product" style="left:802px">
    <div class="product-photo" role="img" aria-label="White tea towel with grey lettered stripe on a white plate" style="background:linear-gradient(180deg,#e6e4df,#d6d3cc 50%,#b4b0a6)"></div>
    <div class="product-brand">Simple As You Go</div>
    <div class="product-name">Popcorn Stitch Cardigan</div>
    <div class="price">€ 42<sup>.35</sup></div>
  </article>
</div>
</body>
</html>
```